Plumbing Service Flyer Needed For Swapboard

Plumbing ad needs to be effective (600 by 450 pixels)
Ad must include company name Plumbing Aces and phone number 202-555-0187
No URLs, links, or web addresses in your text or image please.

(about us we offer a wide range of plumbing services from emergency plumbing to commercial plumbing services, our master plumbers are ready to handle all jobs, large or small, at anytime during the day or night. Pickup the phone and call us today).

Target Market(s)

DC Metro Area

Industry/Entity Type

Plumbing

Font styles to use
Other font styles liked:
• No preference. Let the designer choose

Colors

Designer to choose colors to be used in the design.

Requirements
Must have
• 1. A bold headline: headline should communicate what my business is all about.
• 2. Great photography
• 3. Discounts or specials
• 4. Call to action
• 5. Key facts: Let consumers know about the product or service (see attached ad)
• 6. Good graphics
Should not have
• No URLs, links, or web addresses in your text or image please.

```html
<!DOCTYPE html>
<html lang="en">
<head>
<meta charset="utf-8">
<title>Plumbing Aces – Service Flyer</title>
<link rel="stylesheet" href="https://fonts.googleapis.com/css2?family=Montserrat:wght@600;700;800&family=Lato:wght@400;700&display=swap">
<style>
  :root {
    --brand-blue: #0a5bb0;
    --brand-blue-deep: #0b4c95;
    --ink-gray: #555759;
    --ink-dark: #222426;
    --accent-yellow: #f3ea3a;
    --strip-gray: #e3e4e5;
    --tab-gray: #9a9c9e;
    --bar-dark: #303132;
    --paper: #ffffff;
    --canvas-bg: #e9eaeb;
    --gold: #d9b12a;
    --gold-deep: #a57c12;
  }
  * { box-sizing: border-box; margin: 0; padding: 0; }
  html, body { width: 1200px; height: 1200px; overflow: hidden; }
  body { background: var(--canvas-bg); font-family: "Lato", sans-serif; }

  .flyer {
    position: absolute; left: 40px; top: 180px;
    width: 1120px; height: 839px;
    background: var(--paper); overflow: hidden;
    box-shadow: 0 6px 24px rgba(0,0,0,.18);
  }

  .headline { position: absolute; left: 295px; top: 36px; font-family: "Montserrat", sans-serif; font-weight: 800; line-height: 1; z-index: 2; }
  .headline-top { display: block; color: var(--brand-blue); font-size: 47px; letter-spacing: .3px; }
  .headline-main { display: block; color: var(--ink-gray); font-size: 61px; margin-top: 6px; letter-spacing: .6px; }

  .intro-band {
    position: absolute; left: 165px; top: 176px; width: 918px; height: 202px;
    background: linear-gradient(90deg, var(--brand-blue-deep), var(--brand-blue) 60%, #1a6cc4);
    padding: 21px 20px 0 132px; color: #fff; font-size: 22.5px; line-height: 29px;
  }
  .intro-band p + p { margin-top: 14px; }
  .intro-band .highlight { color: var(--accent-yellow); font-weight: 700; }

  .plumber-photo {
    position: absolute; left: 0; top: 69px; width: 368px; height: 694px; z-index: 1;
    background: linear-gradient(180deg, #dfe6ef 0%, #2c3f73 30%, #1f2f5e 100%);
    clip-path: polygon(0 0, 76% 0, 76% 46%, 100% 56%, 100% 100%, 0 100%);
  }

  .services-title {
    position: absolute; left: 379px; top: 392px; display: flex; align-items: center; width: 704px;
    font-family: "Montserrat", sans-serif; font-weight: 700; font-size: 31px; color: var(--ink-dark);
  }
  .services-title::after { content: ""; flex: 1; height: 1px; background: #c5c7c9; margin-left: 22px; }

  .service-list { position: absolute; list-style: none; font-size: 24px; color: var(--ink-dark); }
  .service-list li { position: relative; padding-left: 36px; line-height: 31px; }
  .service-list li svg { position: absolute; left: 0; top: 6px; width: 20px; height: 20px; }
  .service-list.left { left: 400px; top: 436px; }
  .service-list.left li + li { margin-top: 11.5px; }
  .service-list.right { left: 763px; top: 436px; width: 322px; }
  .service-list.right li { text-align: justify; line-height: 31px; }
  .service-list.right li.single { text-align-last: justify; }
  .service-list.right li + li { margin-top: 8px; }

  .call-tab {
    position: absolute; left: 379px; top: 665px; width: 296px; height: 38px;
    background: var(--tab-gray); border-radius: 0 22px 0 0;
    color: #fff; font-family: "Montserrat", sans-serif; font-weight: 600; font-size: 26px;
    padding-left: 32px; line-height: 38px;
  }
  .phone-strip { position: absolute; left: 379px; top: 703px; width: 741px; height: 61px; background: var(--strip-gray); }
  .phone-number {
    position: absolute; left: 486px; top: 708px; display: flex; align-items: center; gap: 18px;
    font-family: "Montserrat", sans-serif; font-weight: 700; font-size: 38px; color: var(--ink-dark);
  }
  .phone-number svg { width: 44px; height: 44px; }

  .guarantee-seal { position: absolute; left: 197px; top: 599px; width: 178px; height: 178px; z-index: 3; }
  .hours-badge { position: absolute; left: 950px; top: 640px; width: 134px; height: 134px; z-index: 3; }

  .footer-bar {
    position: absolute; left: 0; top: 764px; width: 1120px; height: 75px; background: var(--bar-dark);
    color: #fff; font-family: "Montserrat", sans-serif; font-weight: 600; font-size: 27px;
    display: flex; align-items: center; justify-content: center; gap: 10px; z-index: 2;
  }
  .footer-bar .company { color: #f6f1a6; font-family: "Lato", sans-serif; font-weight: 700; font-size: 29px; }
</style>
</head>
<body>
  <main class="flyer">
    <div class="intro-band">
      <p>The best priced any plumbing repair install or remodel. You only need one call for us to handle it all, super fast, always reliable &amp; affordable plumber.</p>
      <p><span class="highlight">Call us today for same day service.</span> Bonded, licensed and insured. We handle fixes, installation, leaks, remodels, new construction and more! do not use a handyman, use a certified plumber like me.</p>
    </div>

    <div class="plumber-photo" role="img" aria-label="Photo of a smiling plumber in a navy cap and coveralls, arms crossed, holding a red pipe wrench"></div>

    <h1 class="headline">
      <span class="headline-top">NEED A PROFFESSIONAL</span>
      <span class="headline-main">PLUMBING SERVICES?</span>
    </h1>

    <h2 class="services-title">OUR SERVICES</h2>

    <ul class="service-list left">
      <li><svg viewBox="0 0 20 20"><rect x="1.5" y="3" width="15" height="15" fill="none" stroke="#0a5bb0" stroke-width="2"/><path d="M5 10l4 4 9-11" fill="none" stroke="#0a5bb0" stroke-width="2.2"/></svg>Plumbing clogs</li>
      <li><svg viewBox="0 0 20 20"><rect x="1.5" y="3" width="15" height="15" fill="none" stroke="#0a5bb0" stroke-width="2"/><path d="M5 10l4 4 9-11" fill="none" stroke="#0a5bb0" stroke-width="2.2"/></svg>Water heater replacement</li>
      <li><svg viewBox="0 0 20 20"><rect x="1.5" y="3" width="15" height="15" fill="none" stroke="#0a5bb0" stroke-width="2"/><path d="M5 10l4 4 9-11" fill="none" stroke="#0a5bb0" stroke-width="2.2"/></svg>Repair &amp; install gas lines</li>
      <li><svg viewBox="0 0 20 20"><rect x="1.5" y="3" width="15" height="15" fill="none" stroke="#0a5bb0" stroke-width="2"/><path d="M5 10l4 4 9-11" fill="none" stroke="#0a5bb0" stroke-width="2.2"/></svg>Remodel your plumbing</li>
      <li><svg viewBox="0 0 20 20"><rect x="1.5" y="3" width="15" height="15" fill="none" stroke="#0a5bb0" stroke-width="2"/><path d="M5 10l4 4 9-11" fill="none" stroke="#0a5bb0" stroke-width="2.2"/></svg>Flood repair</li>
    </ul>

    <ul class="service-list right">
      <li class="single"><svg viewBox="0 0 20 20"><rect x="1.5" y="3" width="15" height="15" fill="none" stroke="#0a5bb0" stroke-width="2"/><path d="M5 10l4 4 9-11" fill="none" stroke="#0a5bb0" stroke-width="2.2"/></svg>Disposals repair &amp; install</li>
      <li class="single"><svg viewBox="0 0 20 20"><rect x="1.5" y="3" width="15" height="15" fill="none" stroke="#0a5bb0" stroke-width="2"/><path d="M5 10l4 4 9-11" fill="none" stroke="#0a5bb0" stroke-width="2.2"/></svg>Toilets install or replace</li>
      <li class="single"><svg viewBox="0 0 20 20"><rect x="1.5" y="3" width="15" height="15" fill="none" stroke="#0a5bb0" stroke-width="2"/><path d="M5 10l4 4 9-11" fill="none" stroke="#0a5bb0" stroke-width="2.2"/></svg>New piping and repairs</li>
      <li><svg viewBox="0 0 20 20"><rect x="1.5" y="3" width="15" height="15" fill="none" stroke="#0a5bb0" stroke-width="2"/><path d="M5 10l4 4 9-11" fill="none" stroke="#0a5bb0" stroke-width="2.2"/></svg>New homes, old homes, commercial plumbing and a ton more</li>
    </ul>

    <div class="call-tab">CALL US TODAY</div>
    <div class="phone-strip"></div>
    <div class="phone-number">
      <svg viewBox="0 0 44 44"><circle cx="22" cy="22" r="19" fill="none" stroke="#0a5bb0" stroke-width="2.5"/><path d="M15 12c1.5-1 3-1 3.6.3l1.6 3.6c.4 1-.2 1.8-1 2.4l-1 .8c1 2.6 3 4.8 5.6 6l.9-1c.7-.8 1.6-1.2 2.5-.7l3.4 1.8c1.2.6 1.1 2.2 0 3.5-1.5 1.8-3.8 2.2-6 1.2-5-2.4-8.8-6.6-10.6-11.6-.7-2.2-.3-4.8 1-6.3z" fill="#0a5bb0"/></svg>
      <span>202-555-0187</span>
    </div>

    <svg class="guarantee-seal" viewBox="0 0 180 180" role="img" aria-label="Satisfaction guarantee seal">
      <circle cx="90" cy="90" r="86" fill="var(--gold)"/>
      <circle cx="90" cy="90" r="70" fill="none" stroke="var(--gold-deep)" stroke-width="3"/>
    </svg>

    <svg class="hours-badge" viewBox="0 0 136 136">
      <circle cx="68" cy="70" r="56" fill="#0a5bb0"/>
      <path d="M22 42a58 58 0 1 0 48-30" fill="none" stroke="#0a5bb0" stroke-width="4"/>
      <path d="M62 4l16 8-16 10z" fill="#0a5bb0"/>
      <text x="31" y="72" fill="#fff" font-family="Montserrat, sans-serif" font-weight="800" font-size="30">24</text>
      <text x="76" y="82" fill="#fff" font-family="Montserrat, sans-serif" font-weight="800" font-size="28">/7</text>
      <text x="33" y="83" fill="#fff" font-family="Lato, sans-serif" font-size="9">HOURS</text>
      <text x="33" y="100" fill="#fff" font-family="Montserrat, sans-serif" font-weight="700" font-size="15">SERVICE</text>
    </svg>

    <footer class="footer-bar">
      <span>SEE ALL OF OUR SERVICES ONLINE AT</span>
      <span class="company">Plumbing Aces</span>
    </footer>
  </main>
</body>
</html>
```